Bref créative
Lemon Badger
Cakes and Desserts
Bright & Fun-filled
Marla Tevison
Owner
2193 Brennick Ct.
Arvada, CO 80005
marla.tevison@postvale.net
Join us on Facebook!
I also need stationery that ties in with my business card.
Logo for cake company

```html
<!DOCTYPE html>
<html lang="en">
<head>
<meta charset="UTF-8">
<title>Lemon Badger — Business Card</title>
<link rel="stylesheet" href="https://fonts.googleapis.com/css2?family=Open+Sans:wght@400;600;700&display=swap">
<style>
  :root {
    --stage: #efe9e3;
    --pink: #e8308f;
    --pink-light: #f58cc0;
    --brown: #6e3a1c;
    --orange: #d9822b;
    --white: #ffffff;
    --grey: #6b6b6b;
  }
  * { margin: 0; padding: 0; box-sizing: border-box; }
  html, body { width: 1200px; height: 646px; overflow: hidden; }
  body {
    background: var(--stage);
    font-family: "Open Sans", Arial, sans-serif;
    display: flex;
    align-items: center;
    justify-content: center;
    gap: 60px;
  }
  .card {
    width: 500px;
    height: 286px;
    border-radius: 6px;
    position: relative;
    overflow: hidden;
    box-shadow: 0 8px 24px rgba(0,0,0,0.15);
  }
  .card-front {
    background: var(--pink);
    display: flex;
    flex-direction: column;
    align-items: center;
    justify-content: center;
    gap: 14px;
  }
  .name-panel {
    background: var(--white);
    border-radius: 14px;
    padding: 18px 34px;
    display: flex;
    flex-direction: column;
    align-items: center;
    gap: 4px;
  }
  .business-name {
    font-weight: 700;
    color: var(--brown);
    font-size: 34px;
    line-height: 1.1;
  }
  .business-type {
    font-size: 13px;
    font-weight: 400;
    color: var(--grey);
  }
  .website {
    color: var(--white);
    font-size: 12px;
    letter-spacing: 2px;
    font-weight: 600;
  }
  .card-back { background: var(--white); }
  .back-name {
    position: absolute;
    left: 28px; top: 92px;
    display: flex;
    flex-direction: column;
    gap: 2px;
  }
  .back-name .business-name { font-size: 26px; }
  .back-name .business-type { font-size: 11px; }
  .cake-art {
    position: absolute;
    right: 40px; top: 24px;
    width: 150px; height: 140px;
    border-radius: 10px;
    background: linear-gradient(180deg, var(--pink-light) 0%, var(--pink) 50%, var(--brown) 100%);
  }
  .contact {
    position: absolute;
    left: 28px; bottom: 26px;
  }
  .contact-name {
    color: var(--orange);
    font-weight: 600;
    font-size: 15px;
    margin-bottom: 4px;
  }
  .contact-line {
    color: var(--grey);
    font-size: 10.5px;
    line-height: 1.5;
  }
</style>
</head>
<body>
  <section class="card card-front">
    <div class="name-panel">
      <div class="business-name">Lemon Badger</div>
      <div class="business-type">Cakes and Desserts</div>
    </div>
    <div class="website">www.lemonbadgercakes.com</div>
  </section>

  <section class="card card-back">
    <div class="cake-art" role="img" aria-label="Illustration of a tiered pink and brown cake"></div>
    <div class="back-name">
      <div class="business-name">Lemon Badger</div>
      <div class="business-type">Cakes and Desserts</div>
    </div>
    <div class="contact">
      <div class="contact-name">Marla Tevison</div>
      <div class="contact-line">(720) 555-0143</div>
      <div class="contact-line">marla.tevison@postvale.net</div>
    </div>
  </section>
</body>
</html>
```